Personal Injury Attorney Marketing Brochure to Medical Providers

We are looking to have a brochure - booklet form - outside - inside and back page - to hand out to chiropractors, physical therapist, clinics and other medical providers that treat persons who were injured - from an auto accident - truck accident - slip and fall, work related injury. We want them to know we handle personal injury work and represent persons who were injured as a result of the negligence of another person / company. We want the brochure to be professional and represent that we have a lot of experience in this area - Brian in practice since 1990 and Lena since 2000. Please refer to our website - www.fenwoodlegal.com for the type of work that we do and the practice areas. If we need to send more content - let us know. The project is to advertise only Brian Tolliver and lena Moskos.
Updates

We added a QR code to add to the brochure

Target Market(s)

Medical providers - such as chiropractors, Physical therapist, orthopedic doctors who may be able to refer a patient to a personal injury attorney who can help them pursue a personal injury claim

Industry/Entity Type

We are personal injury attorneys - we represent persons who have been injured in car accidents, trucking accidents, work site accidents, slip and falls that result in - broken bones, serious injuries and other injuries to help them get compensation

Font styles to use
Serif

Colors
0054AA
0677BA
7BADD7
CADEEF
E8F1F8

Requirements
Must have
• Photos of law firm members Brian Tolliver and Lena Moskos and our firm logo, our l numnew location address - which is 415 Wexbury Mill Rd., Norcross, GA 30071 / our direct phone numbers / e-mail address / website and information about us and our practice / Free consult / Attorney's who are very accessible / We have spanish speaking attorney and staff members. Please use only LEXRA or Google reviews for Brian Tolliver or Lena Moskos - not for Gordon Pellish. For e-mail contact to the firm - add admin@fenwoodlegal or admin3@fenwoodlegal.com - and add for Spanish - 404-555-0172 or for English - 404-555-0186
Nice to have
• Quotes from satisfied customers from Brian Tolliver and Lena Moskos's Google reviews and LEXRA reviews / our LEXRA ratings - all of which can be found on the internet - or we can provide - see attached word document with Google and LEXRA review information.
Should not have
• No guarantee of results

```html
<!DOCTYPE html>
<html lang="en">
<head>
<meta charset="utf-8">
<title>Pellish Tolliver Moskos – Injury Lawyers Brochure</title>
<link rel="stylesheet" href="https://fonts.googleapis.com/css2?family=Libre+Baskerville:ital,wght@0,400;0,700;1,400&family=Open+Sans:wght@400;600;700&display=swap">
<style>
:root{
  --bg:#e7e7e6;
  --navy:#1f3566;
  --navy-deep:#172a54;
  --blue:#0054AA;
  --blue-mid:#0677BA;
  --blue-panel:#3f74b6;
  --blue-soft:#7BADD7;
  --blue-pale:#CADEEF;
  --blue-mist:#E8F1F8;
  --pill:#5b8fd0;
  --ink:#3a3f4a;
  --grey:#8a8f98;
  --white:#ffffff;
  --serif:"Libre Baskerville", Georgia, serif;
  --sans:"Open Sans", Arial, sans-serif;
}
*{box-sizing:border-box;margin:0;padding:0}
html,body{width:1200px;height:2606px;overflow:hidden;background:var(--bg)}
.canvas{position:relative;width:1200px;height:2606px}
.page{position:absolute;width:520px;height:735px;overflow:hidden;background:var(--white);box-shadow:0 6px 18px rgba(0,0,0,.18)}
.page-art{position:absolute;left:0;top:0;width:520px;height:735px}
.spread{position:absolute;width:1040px;height:735px}
.spread .page:first-child{left:0}
.spread .page:last-child{left:520px}
.spread .page:first-child::after{content:"";position:absolute;right:0;top:0;width:26px;height:100%;background:linear-gradient(to left,rgba(0,0,0,.12),transparent)}
.spread .page:last-child::after{content:"";position:absolute;left:0;top:0;width:26px;height:100%;background:linear-gradient(to right,rgba(0,0,0,.12),transparent)}

/* firm name */
.firm{position:absolute;display:flex;align-items:center;gap:10px}
.firm-square{width:14px;height:14px;background:var(--navy)}
.firm-name{font-family:var(--serif);font-weight:700;color:var(--navy);font-size:19px;letter-spacing:.5px;white-space:nowrap}
.firm-sub{position:absolute;font-family:var(--serif);font-size:9px;letter-spacing:4px;color:var(--grey)}

/* cover */
.cover-title{position:absolute;left:40px;width:460px;text-align:center;color:var(--white)}
.cover-title h1{font-family:var(--serif);font-weight:700;font-size:25px;line-height:1.2}
.cover-title .tagline{margin-top:8px;font-family:var(--sans);font-size:10px;letter-spacing:1.5px;color:var(--blue-soft)}
.pill{position:absolute;height:20px;border-radius:10px 10px 0 0;background:var(--pill);color:var(--white);font-family:var(--sans);font-size:9px;letter-spacing:2px;text-align:center;line-height:20px}

/* back page */
.team-title{position:absolute;top:70px;left:0;width:520px;text-align:center;font-family:var(--serif);color:var(--white);font-size:17px;letter-spacing:3px}
.attorney{position:absolute;width:228px;color:var(--white);font-family:var(--sans)}
.attorney-head{display:flex;gap:12px;align-items:center}
.portrait{width:64px;height:64px;border-radius:50%;border:3px solid var(--white);flex:none}
.attorney h3{font-family:var(--serif);font-weight:400;font-size:14px}
.attorney .role{font-size:8px;color:var(--blue-pale);margin-bottom:4px}
.contact-line{display:flex;align-items:center;gap:5px;font-size:7.5px;line-height:1.6}
.contact-line svg{width:8px;height:8px;flex:none}
.bio{margin-top:12px;font-size:6.6px;line-height:1.55;color:var(--blue-mist)}
.bio p+p{margin-top:5px}
.stars{margin-top:8px;font-size:9px;letter-spacing:2px;color:var(--white)}
.badges{display:flex;gap:6px;margin-top:8px}
.badge{width:26px;height:18px;background:var(--blue-mist);border-radius:2px}
.badge.round{width:18px;border-radius:50%}
.back-quote{position:absolute;left:24px;top:606px;font-family:var(--serif);font-size:7.5px;color:var(--blue-soft);letter-spacing:.6px}
.back-contact{position:absolute;left:270px;top:640px;color:var(--white);font-family:var(--sans);font-size:7.5px;line-height:1.7}
.back-contact strong{font-family:var(--serif);font-weight:400;font-size:9px;letter-spacing:.8px;display:block;margin-bottom:2px}
.back-contact .contact-line{font-size:7.5px}

/* inside pages */
.inside-h{font-family:var(--serif);font-weight:700;color:var(--navy);font-size:10px;line-height:1.45;text-transform:uppercase}
.body-copy{font-family:var(--sans);font-size:6.8px;line-height:1.6;color:var(--ink)}
.body-copy p+p{margin-top:6px}
.block{position:absolute}
.icon-row{display:flex;gap:10px;align-items:flex-start;margin-top:9px}
.icon-row svg{width:18px;height:18px;flex:none}
.areas{position:absolute;left:0;top:212px;width:520px;height:230px}
.areas h2{position:absolute;top:18px;left:0;width:520px;text-align:center;font-family:var(--serif);font-weight:400;font-size:12px;letter-spacing:2.5px;color:var(--blue-soft)}
.areas-list{position:absolute;top:46px;left:34px;width:460px;display:grid;grid-template-columns:repeat(3,1fr);gap:0 14px}
.areas-list ul{list-style:none;font-family:var(--sans);font-size:7.2px;line-height:1.85;color:var(--white)}
.areas-list li::before{content:"• ";color:var(--blue-soft)}
.closing{font-family:var(--serif);font-size:7.5px;color:var(--blue-mid);letter-spacing:.5px;margin-top:8px}
.photo-firm{position:absolute;left:60px;top:80px;font-family:var(--serif);font-weight:700;font-size:24px;color:rgba(31,53,102,.55)}
</style>
</head>
<body>
<main class="canvas">

  <!-- Cover (single) -->
  <section class="page cover" style="left:340px;top:90px">
    <svg class="page-art" viewBox="0 0 520 735">
      <defs>
        <linearGradient id="paperA" x1="0" y1="0" x2="1" y2="1"><stop offset="0" stop-color="#ffffff"/><stop offset="1" stop-color="#eef1f5"/></linearGradient>
        <linearGradient id="roadA" x1="0" y1="0" x2="1" y2="1"><stop offset="0" stop-color="#b9a678"/><stop offset=".45" stop-color="#cdbfa2"/><stop offset=".7" stop-color="#dcdcdc"/><stop offset="1" stop-color="#a9acb0"/></linearGradient>
      </defs>
      <rect width="520" height="735" fill="url(#paperA)"/>
      <path role="img" aria-label="Photo: young woman sitting distressed beside a car with a flat tyre on a dirt roadside" d="M0,172 C150,212 360,167 520,102 L520,620 L0,620Z" fill="url(#roadA)"/>
      <path d="M0,168 C150,208 360,163 520,98" fill="none" stroke="#1f3566" stroke-width="7"/>
      <path d="M0,180 C150,221 360,176 520,111" fill="none" stroke="#0677BA" stroke-width="3"/>
      <path d="M0,598 C190,588 380,533 520,443" fill="none" stroke="#3f7cc8" stroke-width="7"/>
      <path d="M0,608 C190,598 380,543 520,453 L520,735 L0,735Z" fill="#1f3566"/>
    </svg>
    <div class="firm" style="left:50px;top:60px"><span class="firm-square"></span><span class="firm-name">PELLISH TOLLIVER MOSKOS</span></div>
    <div class="firm-sub" style="left:150px;top:90px">ATTORNEYS AT LAW</div>
    <div class="cover-title" style="top:632px"><h1>Dedicated Georgia Injury Lawyers</h1><p class="tagline">DRIVEN. ATTENTIVE. RELIABLE.</p></div>
    <div class="pill" style="left:150px;bottom:0;width:220px">www.fenwoodlegal.com</div>
  </section>

  <!-- Back + Front spread -->
  <section class="spread" style="left:80px;top:935px">
    <article class="page back">
      <svg class="page-art" viewBox="0 0 520 735">
        <defs>
          <linearGradient id="panelB" x1="0" y1="0" x2="0" y2="1"><stop offset="0" stop-color="#4a80c2"/><stop offset="1" stop-color="#2f5c9c"/></linearGradient>
        </defs>
        <rect width="520" height="735" fill="#eef1f5"/>
        <path d="M0,48 C180,40 360,36 520,30 L520,735 L0,735Z" fill="url(#panelB)"/>
        <path d="M0,580 C160,560 360,560 520,610" fill="none" stroke="#CADEEF" stroke-width="3"/>
        <path d="M0,590 C160,570 360,570 520,620 L520,735 L0,735Z" fill="#1f3566"/>
      </svg>
      <h2 class="team-title">MEET OUR TEAM</h2>

      <div class="attorney" style="left:24px;top:112px">
        <div class="attorney-head">
          <div class="portrait" role="img" aria-label="Portrait photo of attorney Brian Tolliver" style="background:linear-gradient(#b9c6d6,#3b4a64)"></div>
          <div>
            <h3>Brian Tolliver</h3><p class="role">Partner</p>
            <div class="contact-line"><svg viewBox="0 0 10 10"><path d="M2,1 L4,1 L5,3 L4,4 Q5,6 6,6 L7,5 L9,6 L9,8 Q5,9 1,3Z" fill="#fff"/></svg>404-555-0186</div>
            <div class="contact-line"><svg viewBox="0 0 10 10"><rect x="1" y="2" width="8" height="6" fill="none" stroke="#fff"/><path d="M1,2 L5,5 L9,2" fill="none" stroke="#fff"/></svg>admin@fenwoodlegal</div>
          </div>
        </div>
        <div class="bio">
          <p>Brian has practiced personal injury law since 1990. He works closely with injured clients and their medical providers, keeping every file organised and every caller answered promptly.</p>
          <p>He handles auto, truck, slip and fall and work injury claims, and believes that clear communication with treating doctors, chiropractors and therapists helps patients recover with less stress. Free consultations are always available.</p>
        </div>
        <div class="stars">★★★★★</div>
        <div class="badges"><span class="badge"></span><span class="badge round"></span><span class="badge"></span><span class="badge"></span></div>
      </div>

      <div class="attorney" style="left:270px;top:160px">
        <div class="attorney-head">
          <div class="portrait" role="img" aria-label="Portrait photo of attorney Lena Moskos" style="background:linear-gradient(#d9b99a,#5a3a3a)"></div>
          <div>
            <h3>Lena Moskos</h3><p class="role">Partner</p>
            <div class="contact-line"><svg viewBox="0 0 10 10"><path d="M2,1 L4,1 L5,3 L4,4 Q5,6 6,6 L7,5 L9,6 L9,8 Q5,9 1,3Z" fill="#fff"/></svg>404-555-0172</div>
            <div class="contact-line"><svg viewBox="0 0 10 10"><rect x="1" y="2" width="8" height="6" fill="none" stroke="#fff"/><path d="M1,2 L5,5 L9,2" fill="none" stroke="#fff"/></svg>admin3@fenwoodlegal.com</div>
          </div>
        </div>
        <div class="bio">
          <p>Lena has represented injured people since 2000. She speaks Spanish and guides families through every step of a claim, from the first call to the final resolution.</p>
          <p>Clients value her patience and accessibility, and referring providers know she will return calls and share updates about the progress of each case.</p>
        </div>
        <div class="stars">★★★★★</div>
      </div>

      <p class="back-quote">TO US, THE PROCESS MATTERS JUST AS MUCH AS THE END RESULT.</p>
      <div class="firm" style="left:24px;top:650px"><span class="firm-name" style="color:#fff;font-size:13px">PELLISH TOLLIVER MOSKOS</span></div>
      <div class="back-contact">
        <strong>CALL US TODAY • SE HABLA ESPAÑOL</strong>
        <div class="contact-line"><svg viewBox="0 0 10 10"><path d="M2,1 L4,1 L5,3 L4,4 Q5,6 6,6 L7,5 L9,6 L9,8 Q5,9 1,3Z" fill="#7BADD7"/></svg>English 404-555-0186 · Español 404-555-0172</div>
        <div class="contact-line"><svg viewBox="0 0 10 10"><path d="M5,9 L2,5 A3,3 0 1 1 8,5Z" fill="#7BADD7"/></svg>415 Wexbury Mill Rd., Norcross, GA 30071</div>
      </div>
      <div class="pill" style="left:130px;bottom:0;width:220px">www.fenwoodlegal.com</div>
    </article>

    <article class="page cover">
      <svg class="page-art" viewBox="0 0 520 735">
        <defs>
          <linearGradient id="paperC" x1="0" y1="0" x2="1" y2="1"><stop offset="0" stop-color="#ffffff"/><stop offset="1" stop-color="#eef1f5"/></linearGradient>
          <linearGradient id="roadC" x1="0" y1="0" x2="1" y2="1"><stop offset="0" stop-color="#b9a678"/><stop offset=".45" stop-color="#cdbfa2"/><stop offset=".7" stop-color="#dcdcdc"/><stop offset="1" stop-color="#a9acb0"/></linearGradient>
        </defs>
        <rect width="520" height="735" fill="url(#paperC)"/>
        <path role="img" aria-label="Photo: young woman sitting distressed beside a car with a flat tyre on a dirt roadside" d="M0,172 C150,212 360,167 520,102 L520,620 L0,620Z" fill="url(#roadC)"/>
        <path d="M0,168 C150,208 360,163 520,98" fill="none" stroke="#1f3566" stroke-width="7"/>
        <path d="M0,180 C150,221 360,176 520,111" fill="none" stroke="#0677BA" stroke-width="3"/>
        <path d="M0,598 C190,588 380,533 520,443" fill="none" stroke="#3f7cc8" stroke-width="7"/>
        <path d="M0,608 C190,598 380,543 520,453 L520,735 L0,735Z" fill="#1f3566"/>
      </svg>
      <div class="firm" style="left:50px;top:60px"><span class="firm-square"></span><span class="firm-name">PELLISH TOLLIVER MOSKOS</span></div>
      <div class="firm-sub" style="left:150px;top:90px">ATTORNEYS AT LAW</div>
      <div class="cover-title" style="top:632px"><h1>Dedicated Georgia Injury Lawyers</h1><p class="tagline">DRIVEN. ATTENTIVE. RELIABLE.</p></div>
      <div class="pill" style="left:150px;bottom:0;width:220px">www.fenwoodlegal.com</div>
    </article>
  </section>

  <!-- Inside spread -->
  <section class="spread" style="left:80px;top:1780px">
    <article class="page inside-left">
      <svg class="page-art" viewBox="0 0 520 735">
        <defs>
          <linearGradient id="deskL" x1="0" y1="0" x2="1" y2="1"><stop offset="0" stop-color="#1c3350"/><stop offset=".5" stop-color="#4d6580"/><stop offset="1" stop-color="#c9ced4"/></linearGradient>
        </defs>
        <rect width="520" height="735" fill="#f7f8fa"/>
        <path d="M0,262 C170,255 360,228 520,180" fill="none" stroke="#0677BA" stroke-width="4"/>
        <path role="img" aria-label="Photo: lawyer working on a laptop with law and justice icons overlaid" d="M0,270 C170,263 360,236 520,188 L520,470 C360,478 170,480 0,470Z" fill="url(#deskL)"/>
        <path d="M0,476 C170,486 360,484 520,476" fill="none" stroke="#0677BA" stroke-width="3"/>
        <rect x="0" y="718" width="520" height="17" fill="#1f3566"/>
      </svg>
      <div class="block" style="left:30px;top:40px;width:460px">
        <h2 class="inside-h">At Pellish Tolliver Moskos, we see ourselves as a partner in your case, rather than simply a legal expert.</h2>
        <div class="body-copy" style="margin-top:8px">
          <p>We help our clients find solutions to each of their unique legal challenges, with straightforward advice based on in-depth knowledge of Georgia law. We understand how stressful an injury can be, and we take the time to listen.</p>
          <p>We have worked as insurance defense attorneys, so we know how insurers evaluate claims and how to push back when an offer is unfair. That experience lets us prepare every case as if it were going to trial, while still seeking a fair settlement.</p>
          <p>Referring providers can count on prompt updates, and patients can count on attorneys who answer their calls. Contact us today for a free, no-obligation consultation.</p>
        </div>
      </div>
      <div class="block" style="left:30px;top:500px;width:460px">
        <h2 class="inside-h">Our injury law firm has the skill and capacity to handle many different types of cases.</h2>
        <div class="body-copy">
          <div class="icon-row"><svg viewBox="0 0 20 20"><circle cx="10" cy="10" r="9" fill="none" stroke="#1f3566" stroke-width="1.5"/><path d="M6,10 L9,13 L14,7" fill="none" stroke="#1f3566" stroke-width="1.6"/></svg><p>Our attorneys serve clients across metro Atlanta and the surrounding counties, and we are ready to travel to meet injured clients wherever they are recovering.</p></div>
          <div class="icon-row"><svg viewBox="0 0 20 20"><circle cx="10" cy="10" r="9" fill="none" stroke="#1f3566" stroke-width="1.5"/><path d="M6,10 L9,13 L14,7" fill="none" stroke="#1f3566" stroke-width="1.6"/></svg><p>We cover every step of a claim, from gathering medical records and bills to negotiating with insurers and, when needed, presenting the case in court.</p></div>
          <div class="icon-row"><svg viewBox="0 0 20 20"><circle cx="10" cy="10" r="9" fill="none" stroke="#1f3566" stroke-width="1.5"/><path d="M6,10 L9,13 L14,7" fill="none" stroke="#1f3566" stroke-width="1.6"/></svg><p>If you have been injured due to someone else's negligence, we can help you pursue compensation for medical care, lost wages, pain and suffering.</p></div>
        </div>
      </div>
    </article>

    <article class="page inside-right">
      <svg class="page-art" viewBox="0 0 520 735">
        <defs>
          <linearGradient id="armR" x1="0" y1="0" x2="1" y2="0"><stop offset="0" stop-color="#6f8fb8"/><stop offset=".5" stop-color="#d9dee5"/><stop offset="1" stop-color="#9aa3b4"/></linearGradient>
        </defs>
        <rect width="520" height="735" fill="#f7f8fa"/>
        <rect role="img" aria-label="Photo: patient with a bandaged arm in a sling" x="0" y="0" width="520" height="212" fill="url(#armR)"/>
        <rect x="0" y="212" width="520" height="230" fill="#1f3566"/>
        <path d="M0,442 C180,468 360,470 520,440 L520,442 L0,442Z" fill="#1f3566"/>
        <path d="M0,450 C180,476 360,478 520,448" fill="none" stroke="#0677BA" stroke-width="3"/>
        <rect x="0" y="718" width="520" height="17" fill="#1f3566"/>
      </svg>
      <div class="photo-firm">PELLISH TOLLIVER MOSKOS</div>
      <div class="areas">
        <h2>AREAS WE SERVE</h2>
        <div class="areas-list">
          <ul><li>Personal Injury</li><li>Animal Bites</li><li>Autonomous Vehicle Injuries</li><li>Bicycle Accidents</li><li>Boat Accidents</li><li>Burn Injuries</li><li>Car Accidents</li><li>Commercial Truck Accidents</li><li>Construction Injuries</li></ul>
          <ul><li>Distracted Driver Injuries</li><li>Drunk Driver Injuries</li><li>Foodborne Illness</li><li>Food Poisoning</li><li>Fractures/Broken Bones</li><li>Motorcycle Accidents</li><li>Neck Injuries</li><li>Negligent Security</li><li>Nursing Home Abuse and Neglect</li></ul>
          <ul><li>Pedestrian Accidents</li><li>Rear End Accidents</li><li>Rideshare Accidents</li><li>Serious Injuries</li><li>Slip and Fall Accidents</li><li>Spinal Cord Injuries</li><li>Traumatic Brain Injuries</li><li>Wrongful Death</li><li>and much more</li></ul>
        </div>
      </div>
      <div class="block" style="left:34px;top:500px;width:452px">
        <h2 class="inside-h">Why choose us as injury lawyers?</h2>
        <div class="body-copy" style="margin-top:6px">
          <p>If you are searching for experienced, compassionate and results-driven attorneys in Georgia, come to Pellish Tolliver Moskos. We believe in the power of true partnership with every client who contacts us for assistance.</p>
          <p>You will never feel like just another file. Our attorneys are accessible, we return calls quickly, and our Spanish-speaking attorney and staff make sure every client understands each step.</p>
          <p>As a personal injury client, you pay no fees unless we recover compensation for you. Call us for a free consultation and learn how we can help you move forward.</p>
        </div>
        <p class="closing">TO US, THE PROCESS MATTERS JUST AS MUCH AS THE END RESULT.</p>
      </div>
    </article>
  </section>

</main>
</body>
</html>
```